Oversized Post Card for Busines Owners 1st 2nd and 3rd prizes

Create a professional, fresh and polished oversized post card for law firm specializing in Business Law, Succession Planning, and Employment Law

Use any picture(s) of your choice (mine or ones you recommend), logo, headshot and company info

www.morvenquaylegal.example

Westbrook Office - 4175 Hollister Avenue, Suite 1400, Charlotte, NC 28299
Kestrelmoor Office - 13840 Tamsin Way, Suite 300, Charlotte, NC 28296

Phone (704) 555-0187

Use this card for a Free Consultation

Target Market(s)

Business Owners (of small businesses)

Industry/Entity Type

Business

Font styles to use
Serif
Sans Serif

Requirements
Must have
• Company name, logo and contact info
• Serving business owners with legal guidance
• Business Law, Succession Planning & Wealth Transfers
• www.morvenquaylegal.example
• Westbrook Office - 4175 Hollister Avenue, Suite 1400, Charlotte, NC 28299
• Kestrelmoor Office - 13840 Tamsin Way, Suite 300, Charlotte, NC 28296
• Phone (704) 555-0187
• Use this card for a Free Consultation
Nice to have
• pictures (yours or mine) - you choose; headshot picture

```html
<!DOCTYPE html>
<html lang="en">
<head>
<meta charset="utf-8">
<title>Morven Quayle Law PLLC – Postcard</title>
<link href="https://fonts.googleapis.com/css2?family=Raleway:wght@400;500;600;800&display=swap" rel="stylesheet">
<style>
  :root{
    --brand-blue:#12799f;
    --brand-deep:#0b5a7a;
    --brand-navy:#0e3f57;
    --ink:#111;
    --muted:#8a8a8a;
    --paper:#fff;
  }
  *{margin:0;padding:0;box-sizing:border-box}
  html,body{width:1200px;height:771px;overflow:hidden;background:var(--paper)}
  body{font-family:"Raleway",Arial,sans-serif;color:var(--ink)}
  .postcard{position:relative;width:1200px;height:771px;overflow:hidden;background:var(--paper)}
  .hero-art{position:absolute;left:0;top:0}
  .headline{position:absolute;left:304px;top:24px;color:#fff;line-height:1}
  .headline .lead{font-weight:800;font-size:36px;display:block}
  .headline .sub{font-weight:400;font-size:28px;display:block;margin-top:6px;margin-left:20px}

  .headshot{position:absolute;left:792px;top:18px;width:171px;height:169px;border:2px solid var(--brand-blue);padding:5px;background:#fff}
  .headshot-fill{width:100%;height:100%;background:linear-gradient(160deg,#3a3a3a,#caa97a 55%,#e9cfa6)}
  .attorney{position:absolute;left:736px;top:194px;width:282px;text-align:center}
  .attorney-name{color:var(--brand-blue);font-weight:600;font-size:26px}
  .attorney-creds{color:var(--muted);font-size:14px;margin-top:6px}
  .attorney-rule{border-top:2px dotted var(--brand-blue);margin:10px 0 8px}
  .attorney-cert{font-size:15px;line-height:19px;font-weight:500}

  .firm-mark{position:absolute;left:126px;top:258px;width:104px;height:104px;border-radius:50%;background:var(--brand-blue);border:4px solid #d6d6d6;box-shadow:0 0 0 2px var(--brand-navy)}
  .firm-name{position:absolute;left:23px;top:371px;width:310px;border-top:2px solid #222;text-align:center;color:var(--brand-navy);font-weight:500}
  .firm-name .name{display:block;font-size:34px;padding-top:20px;line-height:1}
  .firm-name .suffix{display:flex;align-items:center;gap:10px;font-size:16px;letter-spacing:1px;margin-top:14px}
  .firm-name .suffix::before,.firm-name .suffix::after{content:"";flex:1;border-top:2px solid #222}

  .appointment{position:absolute;left:0;top:510px;width:390px;height:90px;background:var(--brand-blue);clip-path:polygon(0 0,320px 0,390px 90px,0 90px);color:#fff;padding:10px 0 0 23px}
  .appointment .ask{font-size:19px;font-weight:500}
  .appointment .call{font-size:18px;margin-top:2px}
  .appointment .call b{font-size:38px;font-weight:500}

  .offices{position:absolute;top:620px;left:0;width:460px;display:flex}
  .office{width:241px;padding-right:7px;text-align:right}
  .office+.office{width:auto;text-align:left;border-left:1px solid #555;padding:0 0 0 9px}
  .office h3{color:var(--brand-blue);font-weight:600;font-size:19px}
  .office p{color:var(--muted);font-size:14.5px;line-height:19px;margin-top:6px}

  .contact-band{position:absolute;left:0;top:702px;width:514px;height:34px;background:var(--brand-blue);clip-path:polygon(0 0,486px 0,514px 34px,0 34px)}
  .contact-band::before{content:"";position:absolute;left:0;top:0;width:270px;height:34px;background:var(--brand-navy);clip-path:polygon(0 0,244px 0,270px 34px,0 34px)}
  .contact-band span{position:absolute;top:8px;color:#fff;font-size:14px;font-weight:500}
  .contact-band .email{left:14px}
  .contact-band .web{left:276px}
  .offer{position:absolute;left:16px;top:742px;font-size:13px;font-weight:500}

  .services{position:absolute;left:444px;top:318px}
  .services h2{color:var(--brand-blue);font-weight:600;font-size:20px;padding-bottom:5px;border-bottom:2px dotted var(--brand-blue);width:298px}
  .services ul{list-style:none;margin-top:12px}
  .services li{font-size:18px;height:29.3px;display:flex;align-items:center;gap:8px;color:var(--muted)}
  .services li:nth-child(odd){color:var(--brand-blue)}
  .services li svg{width:13px;height:13px;fill:currentColor}
  .divider{position:absolute;left:795px;top:326px;width:2px;height:344px;background:#222}
</style>
</head>
<body>
<main class="postcard">
  <svg class="hero-art" width="800" height="330" viewBox="0 0 800 330">
    <polygon points="0,0 800,0 428,323 0,184" fill="var(--brand-blue)"/>
    <polygon points="0,0 740,0 424,300 0,172" fill="var(--brand-deep)"/>
    <defs>
      <linearGradient id="heroTone" x1="0" y1="0" x2="1" y2="1">
        <stop offset="0" stop-color="#5a5548"/>
        <stop offset="0.45" stop-color="#d8cfae"/>
        <stop offset="1" stop-color="#151515"/>
      </linearGradient>
    </defs>
    <polygon points="0,0 672,0 416,264 0,156" fill="url(#heroTone)" role="img" aria-label="Photo of a row of light bulbs with small figures of people walking among them"/>
  </svg>
  <h1 class="headline"><span class="lead">We will be there</span><span class="sub">when you need us.</span></h1>

  <div class="headshot"><div class="headshot-fill" role="img" aria-label="Headshot portrait of the attorney"></div></div>
  <section class="attorney">
    <div class="attorney-name">Morven A. Quayle</div>
    <div class="attorney-creds">Attorney, CPA, CFM, CMA, MAc.</div>
    <div class="attorney-rule"></div>
    <div class="attorney-cert">Board Certified Specialist in<br>Estate Planning and Probate Law</div>
  </section>

  <div class="firm-mark"></div>
  <div class="firm-name"><span class="name">Morven Quayle</span><span class="suffix">LAW PLLC</span></div>

  <div class="appointment">
    <div class="ask">To schedule an appointment</div>
    <div class="call">call <b>704-555-0187</b></div>
  </div>

  <div class="offices">
    <div class="office"><h3>Westbrook Office</h3><p>4175 Hollister Avenue, Suite 1400<br>Charlotte, NC 28299</p></div>
    <div class="office"><h3>Kestrelmoor Office</h3><p>13840 Tamsin Way, Suite 300<br>Charlotte, NC 28296</p></div>
  </div>

  <div class="contact-band">
    <span class="email">morven@morvenquaylegal.example</span>
    <span class="web">www.morvenquaylegal.example</span>
  </div>
  <p class="offer">Use this card for a Free Consultation</p>

  <section class="services">
    <h2>Other Services We offers :</h2>
    <ul>
      <li><svg viewBox="0 0 10 10"><polygon points="10,0 10,10 0,10"/></svg>Estate Planning</li>
      <li><svg viewBox="0 0 10 10"><polygon points="10,0 10,10 0,10"/></svg>Special Needs Planning</li>
      <li><svg viewBox="0 0 10 10"><polygon points="10,0 10,10 0,10"/></svg>Administration of Estates</li>
      <li><svg viewBox="0 0 10 10"><polygon points="10,0 10,10 0,10"/></svg>Succession Planning</li>
      <li><svg viewBox="0 0 10 10"><polygon points="10,0 10,10 0,10"/></svg>Business Law</li>
      <li><svg viewBox="0 0 10 10"><polygon points="10,0 10,10 0,10"/></svg>Estate, Gift and Income Tax Planning</li>
      <li><svg viewBox="0 0 10 10"><polygon points="10,0 10,10 0,10"/></svg>Estate Disputes</li>
      <li><svg viewBox="0 0 10 10"><polygon points="10,0 10,10 0,10"/></svg>Incompetency Proceedings</li>
      <li><svg viewBox="0 0 10 10"><polygon points="10,0 10,10 0,10"/></svg>Guardianship Proceedings</li>
    </ul>
  </section>
  <div class="divider"></div>
</main>
</body>
</html>
```